Art for parenting podcast with straight/direct talk...no fluff here! "Plain Answers for Families"

I need an image that will not look fluffy or soft. A no-nonsense look. This is not a 'I love parenting' podcast. It is for frustrated parents who don't know what to do. The name is 'Plain Answers for Families'. The design should, therefore, NOT have hearts and flowers but, instead, look clean and direct. My logo has shades of blue so that would be nice. I have done this work for over 30 years and am well-degreed so would like the design to look stable/established. I have attached my company's logo.

Target Market(s)

Frustrated parents of children - age birth to 20

Industry/Entity Type

Coaching/Counseling for parents

Font styles to use
Serif
Sans Serif

Colors
0054AA
0677BA
7BADD7
CADEEF
E8F1F8

Requirements
Must have
• A look that is clean/bold/direct and professional. Serious.
Nice to have
• If it looks good, my name with my degrees behind my name. MS, MEd. Another thought would be to have a background image of a frustrated parent. Not sure if that would be good or look too busy.
Should not have
• Flowers, fluff, soft appearance, pinks, light colors

```html
<!DOCTYPE html>
<html lang="en">
<head>
<meta charset="utf-8">
<title>Plain Answers for Families – Card</title>
<link rel="stylesheet" href="https://fonts.googleapis.com/css2?family=Oswald:wght@400;600&display=swap">
<style>
  :root {
    --backdrop: #d6d6d6;
    --paper: #ffffff;
    --navy: #0054aa;
    --mid-blue: #0677ba;
    --bright-blue: #1a8fd6;
    --sky: #7badd7;
    --frame: #6fb6e0;
    --ghost: #dedede;
    --photo-a: #d9d3cc;
    --photo-b: #9a8576;
  }
  * { margin: 0; padding: 0; box-sizing: border-box; }
  html, body {
    width: 1200px;
    height: 638px;
    overflow: hidden;
    background: var(--backdrop);
    font-family: "Oswald", "Arial Narrow", sans-serif;
  }
  .card {
    position: absolute;
    left: 40px;
    top: 29px;
    width: 1120px;
    height: 580px;
    background: var(--navy);
    overflow: hidden;
  }
  .side-panel {
    position: absolute;
    left: 0;
    top: 0;
    width: 330px;
    height: 490px;
    background: var(--paper);
  }
  .brand {
    position: absolute;
    left: 40px;
    top: 56px;
    display: flex;
    align-items: center;
    gap: 12px;
  }
  .brand-dot {
    width: 34px;
    height: 34px;
    border-radius: 50%;
    background: var(--mid-blue);
  }
  .brand-name {
    font-weight: 600;
    font-size: 30px;
    line-height: 1;
    color: var(--mid-blue);
    text-transform: uppercase;
    letter-spacing: 0.5px;
  }
  .ghost-statement {
    position: absolute;
    left: 40px;
    top: 190px;
    width: 250px;
    font-weight: 400;
    font-size: 34px;
    line-height: 1.25;
    color: var(--ghost);
    text-transform: uppercase;
    letter-spacing: 1px;
  }
  .accent-block {
    position: absolute;
    left: 220px;
    top: 380px;
    width: 110px;
    height: 110px;
    background: var(--bright-blue);
  }
  .title-bar {
    position: absolute;
    left: 330px;
    top: 0;
    width: 790px;
    height: 84px;
    background: var(--navy);
    display: flex;
    align-items: center;
    justify-content: flex-end;
    padding-right: 36px;
  }
  .title {
    font-weight: 600;
    font-size: 40px;
    color: var(--paper);
    text-transform: uppercase;
    letter-spacing: 1px;
  }
  .title-rule {
    position: absolute;
    left: 330px;
    top: 84px;
    width: 790px;
    height: 12px;
    background: var(--frame);
  }
  .photo-frame {
    position: absolute;
    left: 410px;
    top: 118px;
    width: 690px;
    height: 410px;
    background: var(--frame);
    padding: 14px;
  }
  .photo {
    width: 100%;
    height: 100%;
    background: linear-gradient(120deg, var(--photo-a) 0%, #c9b9aa 45%, var(--photo-b) 100%);
  }
  .base-band {
    position: absolute;
    left: 0;
    top: 490px;
    width: 410px;
    height: 90px;
    background: var(--mid-blue);
    border-top: 8px solid var(--sky);
  }
</style>
</head>
<body>
  <div class="card">
    <div class="side-panel">
      <div class="brand">
        <span class="brand-dot"></span>
        <span class="brand-name">Brightpath Parenting</span>
      </div>
      <p class="ghost-statement">Child care is an invisible part of the economy</p>
      <div class="accent-block"></div>
    </div>
    <div class="base-band"></div>
    <div class="title-bar">
      <h1 class="title">Plain Answers for Families</h1>
    </div>
    <div class="title-rule"></div>
    <div class="photo-frame">
      <div class="photo" role="img" aria-label="Photo of a teenage girl arguing while her frustrated mother covers her ears at a table"></div>
    </div>
  </div>
</body>
</html>
```